Business Card for: Northbrook Financial Advisory Services Inc.

provide strategic financial advisory services to companies in the areas of corporate finance, mergers and acquisitions, executive coaching and strategic planning

Target Market(s)

Companies, banks, accountants, lawyers

Industry/Entity Type

High end business consulting in corporate finance, mergers and acquisitions, consulting

Contact Information for Business Card

Name of company, Name: xxxxxx xxxxxx , CEO, - phone number: 1-xxx-xxx-xxxx, - email address,

Requirements
Must have
• Must be professional and simple.
Nice to have
• simple, straight graphics, must give the impression that we are trustworthy, professional, competent
Should not have
• loud colors, loud design features

```html
<!DOCTYPE html>
<html lang="en">
<head>
<meta charset="utf-8">
<title>Northbrook Financial Advisory Services Inc. – Business Card</title>
<link rel="stylesheet" href="https://fonts.googleapis.com/css2?family=Poppins:wght@500;600&family=Urbanist:wght@300;400;700&display=swap">
<style>
  :root {
    --backdrop: #2b2b2d;
    --card: #1b1c1e;
    --card-back-dark: #0b0b0c;
    --card-back-light: #3a3a3c;
    --white: #ffffff;
    --grey: #8a8c90;
    --rule: #5b5d61;
    --blue-light: #4cc6e4;
    --blue-mid: #1a9fd4;
    --blue-dark: #0f72b8;
  }
  * { box-sizing: border-box; margin: 0; padding: 0; }
  html, body { width: 1200px; height: 1108px; overflow: hidden; }
  body {
    background: var(--backdrop);
    font-family: "Urbanist", sans-serif;
    position: relative;
  }
  .card {
    position: absolute;
    top: 214px;
    width: 400px;
    height: 680px;
    border-radius: 30px;
    box-shadow: 0 18px 40px rgba(0,0,0,.45);
    overflow: hidden;
  }
  .card-front {
    left: 150px;
    background: var(--card);
    color: var(--white);
    text-align: center;
  }
  .card-back { left: 650px; background: var(--card-back-dark); }

  .brand { margin-top: 150px; }
  .brand-mark {
    width: 34px; height: 34px; border-radius: 50%;
    background: var(--blue-mid);
    margin: 0 auto 18px;
  }
  .brand-name {
    font-family: "Poppins", sans-serif;
    font-weight: 500;
    font-size: 50px;
    line-height: 1;
    letter-spacing: -0.5px;
    color: var(--white);
  }
  .brand-tagline {
    margin-top: 10px;
    font-size: 19px;
    color: var(--grey);
    letter-spacing: .3px;
  }

  .person { margin-top: 128px; }
  .person-name {
    font-size: 38px;
    font-weight: 300;
    line-height: 1.1;
  }
  .person-name strong { font-weight: 700; }
  .person-title {
    margin-top: 4px;
    font-size: 21px;
    color: var(--grey);
  }

  .contact-icons {
    display: flex;
    align-items: center;
    justify-content: center;
    gap: 8px;
    margin-top: 26px;
  }
  .contact-icons .rule { width: 82px; height: 1px; background: var(--rule); }
  .icon {
    width: 38px; height: 38px; border-radius: 5px;
    display: flex; align-items: center; justify-content: center;
  }
  .icon svg { width: 24px; height: 24px; }
  .icon-phone { background: var(--blue-light); }
  .icon-mail { background: var(--blue-mid); }
  .icon-web { background: var(--blue-dark); }

  .contact-list {
    list-style: none;
    margin-top: 20px;
    font-size: 22px;
    line-height: 1.3;
    color: var(--grey);
  }

  .back-pattern {
    position: absolute; inset: 0;
    background: linear-gradient(215deg, var(--card-back-light) 0%, #1c1c1e 45%, var(--card-back-dark) 80%);
  }
  .back-mark {
    position: absolute;
    left: 236px; top: 480px;
    width: 40px; height: 40px; border-radius: 50%;
    background: var(--blue-mid);
  }
</style>
</head>
<body>
  <section class="card card-front">
    <div class="brand">
      <div class="brand-mark"></div>
      <div class="brand-name">Northbrook</div>
      <div class="brand-tagline">Financial Advisory Services Inc.</div>
    </div>

    <div class="person">
      <div class="person-name">Daniel <strong>Hartley</strong></div>
      <div class="person-title">Managing Director</div>
    </div>

    <div class="contact-icons">
      <span class="rule"></span>
      <span class="icon icon-phone">
        <svg viewBox="0 0 24 24" fill="none" stroke="#fff" stroke-width="1.8" stroke-linejoin="round">
          <path d="M5 9c0-2 1.5-3 3-3h8c1.5 0 3 1 3 3l-2 1-1-2H8L7 10z"/>
          <rect x="6" y="11" width="12" height="8" rx="1.5"/>
          <circle cx="12" cy="15" r="1.6"/>
        </svg>
      </span>
      <span class="icon icon-mail">
        <svg viewBox="0 0 24 24" fill="none" stroke="#fff" stroke-width="1.8" stroke-linejoin="round">
          <rect x="4" y="6.5" width="16" height="11" rx="1"/>
          <path d="M4 7l8 6 8-6M4 17l6-5M20 17l-6-5"/>
        </svg>
      </span>
      <span class="icon icon-web">
        <svg viewBox="0 0 24 24" fill="none" stroke="#fff" stroke-width="1.8">
          <circle cx="12" cy="12" r="7.5"/>
          <ellipse cx="12" cy="12" rx="3.2" ry="7.5"/>
          <path d="M4.5 12h15"/>
        </svg>
      </span>
      <span class="rule"></span>
    </div>

    <ul class="contact-list">
      <li>044-987 654 321</li>
      <li>info@northbrookfa.com</li>
      <li>www.northbrookfa.com</li>
    </ul>
  </section>

  <section class="card card-back">
    <div class="back-pattern" role="img" aria-label="Tonal spot-gloss pattern of the company mark repeated across the card back"></div>
    <div class="back-mark"></div>
  </section>
</body>
</html>
```